Premium Gold Vodka Label Design

English ------------------- We need a label for a Vodka Bottle. Its a sparkling premium vodka with gold inside. The design should look premium. We tried it on our selves but it looks horrible. Therefore we need your help. The current name is corvelle K, but we are open for any better suggestion. We attached the selfmade design. The label will be printed on the bottle. We have other design jobs for you (logo, other sorts)! English ------------------------ We need a label for a vodka bottle. This is a premium vodka which is offset with gold. The design should look like this. We have tried so far and failed. That is why we need your support. The name is so far corvelle K. If you have better suggestions we would be pleased about other suggestions / ideas. In the appendix the failed design is stored. The label is to be applied by screen printing. In the case of good work follow-up projects are guaranteed (logo, other varieties, etc)!
Updates

Reason: We need more time for the decision.

Target Market(s)

USA

Colors

Designer to choose colors to be used in the design.

Requirements
Must have
• English ------------------------ The needed text is on our selfmade label that is attached. English ------------------------ The required texts are stored in the attached design.
Nice to have
• English ------------------------ Transparent places are allowed because we want to print the label on the bottom. English ------------------------ As the label is applied by screen printing, transparent areas are also possible.

```html
<!DOCTYPE html>
<html lang="en">
<head>
<meta charset="utf-8">
<title>corvelle K Premium Gold Sparkling Vodka Label</title>
<link rel="stylesheet" href="https://fonts.googleapis.com/css2?family=Cinzel:wght@400;700&display=swap">
<style>
  :root {
    --page: #0d0d0f;
    --label-white: #f7f7f7;
    --label-grey: #e9e9e9;
    --band-dark: #2a2a2b;
    --band-deep: #1b1b1c;
    --gold: #c9a043;
    --gold-deep: #a87c26;
    --ink: #4a4a4a;
    --strip-text: #f2f2f2;
  }
  html, body {
    margin: 0;
    padding: 0;
    width: 1140px;
    height: 1200px;
    overflow: hidden;
    background: var(--page);
  }
  .canvas {
    position: relative;
    width: 1140px;
    height: 1200px;
  }
  .label {
    position: absolute;
    left: 220px;
    top: 55px;
    width: 700px;
    height: 1090px;
    background: linear-gradient(180deg, var(--label-white) 0%, var(--label-grey) 100%);
    font-family: "Cinzel", serif;
    overflow: hidden;
  }
  .label-art {
    position: absolute;
    inset: 0;
  }
  .brand {
    position: absolute;
    left: 0;
    right: 0;
    top: 190px;
    text-align: center;
    font-family: "Cinzel", serif;
    font-weight: 700;
    font-size: 74px;
    letter-spacing: 2px;
    color: var(--gold);
  }
  .product-line {
    position: absolute;
    left: 0;
    right: 0;
    top: 555px;
    text-align: center;
    font-size: 36px;
    color: var(--ink);
    letter-spacing: 1px;
  }
  .product-name {
    position: absolute;
    left: 0;
    right: 0;
    top: 600px;
    text-align: center;
    font-size: 92px;
    font-weight: 700;
    color: var(--gold);
    letter-spacing: 3px;
  }
  .process {
    position: absolute;
    left: 0;
    right: 0;
    top: 825px;
    text-align: center;
    font-size: 26px;
    color: var(--ink);
  }
  .process .amp {
    color: var(--gold);
    font-weight: 700;
    font-size: 34px;
  }
  .origin {
    position: absolute;
    left: 0;
    right: 0;
    top: 878px;
    text-align: center;
    font-size: 16px;
    color: var(--ink);
  }
  .spec-strip {
    position: absolute;
    left: 20px;
    right: 20px;
    bottom: 30px;
    height: 70px;
    background: linear-gradient(180deg, var(--band-dark), var(--band-deep));
    display: flex;
    justify-content: space-between;
    align-items: center;
    padding: 0 40px;
    box-sizing: border-box;
    color: var(--strip-text);
    font-weight: 700;
    font-size: 22px;
  }
</style>
</head>
<body>
<main class="canvas">
  <section class="label">
    <svg class="label-art" width="700" height="1090" viewBox="0 0 700 1090" aria-hidden="true">
      <defs>
        <linearGradient id="bandShade" x1="0" y1="0" x2="0" y2="1">
          <stop offset="0" stop-color="#1c1c1d"/>
          <stop offset="1" stop-color="#3a3a3b"/>
        </linearGradient>
      </defs>
      <!-- top chevron band -->
      <polygon points="0,0 700,0 700,380 350,495 0,380" fill="url(#bandShade)"/>
      <polyline points="20,380 350,488 680,380" fill="none" stroke="#555" stroke-width="6"/>
      <!-- gold frame lines -->
      <line x1="20" y1="20" x2="20" y2="990" stroke="var(--gold)" stroke-width="3"/>
      <line x1="680" y1="20" x2="680" y2="990" stroke="var(--gold)" stroke-width="3"/>
      <line x1="36" y1="420" x2="36" y2="990" stroke="var(--gold-deep)" stroke-width="1.5"/>
      <line x1="664" y1="420" x2="664" y2="990" stroke="var(--gold-deep)" stroke-width="1.5"/>
    </svg>

    <div class="brand">corvelle K</div>

    <p class="product-line">Premium Gold Sparkling</p>
    <h1 class="product-name">VODKA</h1>
    <p class="process">Distilled <span class="amp">&amp;</span> Filtered</p>
    <p class="origin">Made in Germany</p>

    <div class="spec-strip">
      <span>40% Alc/Vol</span>
      <span>200 mL</span>
      <span>80 proof</span>
    </div>
  </section>
</main>
</body>
</html>
```